Creative Alcoholic Beverage Package Design Needed!

We need a packaging design for a new alcoholic beverage, including the brand name. Flavours will include Sangria and Margarita, and future line extensions as well. Package will be a box (see attached dieline and example of a competitive product) in a 3 liter format. The dimensions of the box need to match the dieline, but we can be creative on the printing of the box. The product inside will be of high-quality, so the design needs to match this
Updates

Need extra days to review

Target Market(s)

25 to 40 year old, 70% female, 30% male

Colors

Designer to choose colors to be used in the design.

Requirements
Must have
• Be attractive, colourful, modern
• clearly mention the flavour, and show the components of the flavour (Sangria : red wine and citrus) - Margarita (mexican inspiration, lime, etc.)
• Have a clear "brand name" along with the flavours
• Mention the quantity (3 liters), alcohol level : 10% alc./vol.

```html
<!DOCTYPE html>
<html lang="en">
<head>
<meta charset="utf-8">
<title>Solvane Margarita – 3 Litre Cask Packaging</title>
<link href="https://fonts.googleapis.com/css2?family=Oranienbaum&family=Oswald:wght@300;400&family=Libre+Baskerville&family=Pinyon+Script&family=Mrs+Saint+Delafield&family=Lato:wght@400&family=Montserrat:wght@400;500&family=Playfair+Display:wght@700&display=swap" rel="stylesheet">
<style>
  :root {
    --backdrop: #a9a3b3;
    --paper: #ffffff;
    --brand-green: #3f7d1f;
    --deep-green: #1f4d0e;
    --mid-green: #4d8f2a;
    --bright-green: #7cbf3a;
    --seal-green: #6db33f;
    --olive-text: #6e6a1c;
    --pale-yellow: #ede59e;
    --icon-olive: #a89d58;
    --cask-green: #a6d36d;
    --ink: #1a1a1a;
    --code-grey: #bdbdbd;
    --photo-lime: #e9e48a;
  }
  * { box-sizing: border-box; margin: 0; padding: 0; }
  html, body { width: 1200px; height: 1200px; overflow: hidden; background: var(--backdrop); }
  .canvas { position: relative; width: 1200px; height: 1200px; background: var(--backdrop); }
  .panel { position: absolute; background: var(--paper); overflow: hidden; }
  .abs { position: absolute; }

  .brand-name { font-family: "Oranienbaum", serif; font-weight: 400; color: var(--brand-green); line-height: 1; white-space: nowrap; }
  .tagline { font-family: "Libre Baskerville", serif; color: var(--ink); white-space: nowrap; text-transform: uppercase; line-height: 1; }
  .flavour-band { position: absolute; }
  .flavour-band .rule { position: absolute; left: 0; background: var(--deep-green); }
  .flavour-band .bar {
    position: absolute; left: 0; display: flex; align-items: center; justify-content: center;
    background: linear-gradient(90deg, var(--mid-green), var(--deep-green));
    color: #fff; font-family: "Oswald", sans-serif; font-weight: 300; white-space: nowrap;
  }
  .contains-title { font-family: "Pinyon Script", cursive; color: var(--brand-green); white-space: nowrap; line-height: 1; }
  .contains-list { list-style: none; font-family: "Libre Baskerville", serif; color: var(--brand-green); text-transform: uppercase; white-space: nowrap; }
  .contains-list li::before { content: "• "; }
  .motif { background: #2b2b2b; border-radius: 40% 40% 50% 50%; }
  .seal { border: 3px solid var(--seal-green); border-radius: 50%; }
  .seal::after { content: ""; position: absolute; inset: 14%; border: 2px solid var(--seal-green); border-radius: 50%; }
  .volume-number { font-family: "Playfair Display", serif; font-weight: 700; color: #000; line-height: 1; font-variant-numeric: lining-nums; font-feature-settings: "lnum" 1; }
  .volume-unit { font-family: "Oswald", sans-serif; font-weight: 300; color: #000; line-height: 1; white-space: nowrap; }
  .served { font-family: "Montserrat", sans-serif; font-weight: 500; color: #000; white-space: nowrap; line-height: 1; }
  .abv { font-family: "Oswald", sans-serif; font-weight: 300; color: #000; white-space: nowrap; line-height: 1; }

  /* front face */
  .front { left: 458px; top: 299px; width: 610px; height: 862px; }
  .front .cocktail-photo {
    left: 140px; top: 240px; width: 470px; height: 622px;
    background: radial-gradient(ellipse 55% 35% at 48% 45%, var(--photo-lime) 0%, #f3efbe 45%, rgba(255,255,255,0) 100%);
  }

  /* lid flap */
  .lid { left: 497px; top: 29px; width: 533px; height: 249px; }
  .lid .code-box { left: 360px; top: 158px; width: 173px; height: 74px; background: var(--code-grey); }
  .lid .code-label { font-family: "Montserrat", sans-serif; font-weight: 500; font-size: 5.5px; letter-spacing: .5px; right: 6px; top: 149px; color: #333; }

  /* side face */
  .side { left: 78px; top: 218px; width: 325px; height: 912px; }
  .side .headline { font-family: "Mrs Saint Delafield", cursive; font-weight: 400; font-size: 46px; line-height: 1; color: #111; width: 100%; text-align: center; top: 46px; }
  .side .copy { left: 28px; width: 270px; font-family: "Lato", sans-serif; font-size: 13.2px; line-height: 18.6px; color: var(--olive-text); text-align: center; }
  .side .pairing-title { width: 100%; text-align: center; top: 457px; font-family: "Montserrat", sans-serif; font-size: 15px; letter-spacing: 2.5px; color: #111; }
  .side .pairing-strip { left: 0; top: 486px; width: 322px; height: 67px; background: var(--pale-yellow); }
  .pairing-item { position: absolute; top: 10px; width: 80px; margin-left: -40px; text-align: center; }
  .pairing-item .pic { width: 38px; height: 26px; margin: 0 auto; background: var(--icon-olive); border-radius: 50% 50% 8px 8px; }
  .pairing-item .label { margin-top: 11px; font-family: "Lato", sans-serif; font-size: 9.5px; color: var(--icon-olive); }
  .panel-mark { font-family: "Libre Baskerville", serif; font-size: 18px; color: #111; }
  .cask-equation { left: 84px; top: 620px; width: 152px; height: 78px; background: var(--cask-green); }
  .cask-equation .mini-pack { left: 6px; top: 8px; width: 38px; height: 48px; background: linear-gradient(160deg, #fff 40%, var(--photo-lime)); border: 1px solid #6a8f3a; }
  .cask-equation .eq { font-family: "Lato", sans-serif; color: #111; white-space: nowrap; }
  .cask-equation .bottle { left: 118px; top: 6px; width: 12px; height: 52px; background: #111; border-radius: 4px 4px 2px 2px; }
  .cask-equation .bottle::before { content: ""; position: absolute; left: 4px; top: -6px; width: 4px; height: 10px; background: #111; }
  .open-here { font-family: "Montserrat", sans-serif; font-size: 10px; letter-spacing: 2px; color: #111; white-space: nowrap; }
  .vertical-brand { transform-origin: left top; transform: rotate(-90deg); }
</style>
</head>
<body>
<div class="canvas">

  <!-- Side face -->
  <section class="panel side" aria-label="Side panel">
    <h2 class="abs headline">Stay Fresh !</h2>
    <p class="abs copy" style="top:124px;">Lorem ipsum dolor sit amet, consectetuer adipiscing elit, sed diam nonummy nibh euismod tincidunt ut laoreet dolore magna aliquam erat volutpat.</p>
    <p class="abs copy" style="top:218px;">Ut wisi enim ad minim veniam, quis nostrud exerci tation ullamcorper suscipit lobortis nisl ut aliquip ex ea commodo consequat. Duis autem vel eum iriure dolor in hendrerit in vulputate velit esse molestie consequat,</p>

    <div class="flavour-band" style="left:0;top:334px;width:325px;height:106px;">
      <div class="rule" style="top:0;width:325px;height:5px;background:linear-gradient(90deg,var(--deep-green),var(--bright-green),var(--deep-green));"></div>
      <div class="bar" style="top:10px;width:325px;height:84px;font-size:37px;letter-spacing:8px;background:radial-gradient(ellipse at 50% 60%,var(--bright-green),var(--mid-green) 70%);">MARGARITA</div>
      <div class="rule" style="top:100px;width:325px;height:5px;background:linear-gradient(90deg,var(--deep-green),var(--bright-green),var(--deep-green));"></div>
    </div>

    <p class="abs pairing-title">Taste Well With</p>
    <div class="abs pairing-strip">
      <div class="pairing-item" style="left:66px;"><div class="pic" role="img" aria-label="Leafy vegetables icon"></div><div class="label">Veggies</div></div>
      <div class="pairing-item" style="left:162px;"><div class="pic" role="img" aria-label="Roast chicken icon"></div><div class="label">Chicken</div></div>
      <div class="pairing-item" style="left:257px;"><div class="pic" role="img" aria-label="Guacamole bowl with chips icon"></div><div class="label">Guacamole</div></div>
    </div>

    <span class="abs panel-mark" style="left:228px;top:582px;">B</span>
    <div class="abs cask-equation">
      <div class="abs mini-pack" role="img" aria-label="Miniature of the cask front"></div>
      <span class="abs eq" style="left:50px;top:26px;font-size:14px;">=</span>
      <span class="abs eq" style="left:74px;top:14px;font-size:26px;">4 x</span>
      <div class="abs bottle" role="img" aria-label="Wine bottle"></div>
      <span class="abs eq" style="left:9px;top:62px;font-size:9.5px;">1 cask&nbsp;&nbsp;&nbsp;=&nbsp;&nbsp;&nbsp;Four 750ml Bottles</span>
    </div>

    <span class="abs panel-mark" style="left:189px;top:742px;">A</span>
    <span class="abs open-here" style="left:129px;top:786px;">OPEN HERE</span>
    <span class="abs abv" style="left:137px;top:803px;font-size:9px;letter-spacing:1px;">10% alc./vol</span>

    <span class="abs volume-number" style="left:32px;top:782px;font-size:54px;">3</span>
    <span class="abs volume-unit" style="left:29px;top:842px;font-size:25px;letter-spacing:3px;">LITERS</span>
    <span class="abs served" style="left:30px;top:873px;font-size:7px;letter-spacing:1.3px;">SERVED CHILLED</span>

    <div class="abs vertical-brand" style="left:262px;top:876px;">
      <div class="brand-name" style="font-size:38px;">Solvane</div>
    </div>
    <div class="abs vertical-brand" style="left:298px;top:876px;">
      <div class="tagline" style="font-size:4px;letter-spacing:.5px;">Love and elegance within yourself</div>
    </div>
  </section>

  <!-- Lid flap -->
  <section class="panel lid" aria-label="Top flap">
    <div class="abs brand-name" style="left:23px;top:8px;font-size:36px;">Solvane</div>
    <div class="abs tagline" style="left:25px;top:47px;font-size:3.8px;letter-spacing:.5px;">Love and elegance within yourself</div>
    <div class="abs motif" style="left:28px;top:81px;width:42px;height:22px;" role="img" aria-label="Agave, sombrero and lime slice motif"></div>
    <div class="abs contains-title" style="left:29px;top:111px;font-size:12px;">Contains</div>
    <ul class="abs contains-list" style="left:31px;top:125px;font-size:6.5px;line-height:8.4px;">
      <li>Mexican inspiration</li><li>Tequila</li><li>Lime juice</li>
    </ul>
    <div class="flavour-band" style="left:0;top:173px;width:140px;height:55px;">
      <div class="rule" style="top:0;width:138px;height:3px;"></div>
      <div class="bar" style="top:6px;width:136px;height:42px;font-size:20px;letter-spacing:4px;clip-path:polygon(0 0,100% 0,97% 100%,0 100%);">MARGARITA</div>
      <div class="rule" style="top:51px;width:134px;height:3px;"></div>
    </div>
    <div class="abs seal" style="left:410px;top:16px;width:104px;height:104px;" role="img" aria-label="Quality seal"></div>
    <span class="abs code-label">BEST BEFORE/PRODUCTION CODE</span>
    <div class="abs code-box"></div>
  </section>

  <!-- Front face -->
  <section class="panel front" aria-label="Front panel">
    <div class="abs cocktail-photo" role="img" aria-label="Photograph of a margarita in a cocktail glass with a green leaf garnish"></div>
    <h1 class="abs brand-name" style="left:0;width:536px;text-align:center;top:62px;font-size:140px;">Solvane</h1>
    <p class="abs tagline" style="left:0;width:536px;text-align:center;top:204px;font-size:13px;letter-spacing:2.6px;">Love and elegance within yourself</p>

    <div class="flavour-band" style="left:0;top:315px;width:256px;height:100px;">
      <div class="rule" style="top:0;width:254px;height:5px;"></div>
      <div class="bar" style="top:10px;width:252px;height:80px;font-size:40px;letter-spacing:8px;clip-path:polygon(0 0,100% 0,97% 100%,0 100%);">MARGARITA</div>
      <div class="rule" style="top:94px;width:244px;height:5px;"></div>
    </div>

    <div class="abs motif" style="left:38px;top:501px;width:94px;height:48px;" role="img" aria-label="Agave, sombrero and lime slice motif"></div>
    <div class="abs contains-title" style="left:40px;top:564px;font-size:26px;">Contains</div>
    <ul class="abs contains-list" style="left:47px;top:593px;font-size:13.5px;line-height:18px;">
      <li>Mexican inspiration</li><li>Tequila</li><li>Lime juice</li>
    </ul>

    <div class="abs seal" style="left:410px;top:593px;width:114px;height:114px;" role="img" aria-label="Quality seal"></div>

    <span class="abs volume-number" style="left:40px;top:706px;font-size:76px;">3</span>
    <span class="abs volume-unit" style="left:40px;top:790px;font-size:32px;letter-spacing:4px;">LITERS</span>
    <span class="abs served" style="left:41px;top:826px;font-size:10px;letter-spacing:2px;">SERVED CHILLED</span>
    <span class="abs abv" style="left:490px;top:798px;font-size:18px;letter-spacing:1.5px;">10% alc./vol</span>
  </section>

</div>
</body>
</html>
```